business card with logo Marigold Nails & Spa 2815 SW Harlow Ave Portland OR 97099

Would like to have a business card with our logo.
like bottle of polish with our logo or letter M on it
want something that first glance would let you know that it is a nail salon.
like the hands with polish bottle dripping.
like black or White back ground

Marigold Nails & Spa
(The Velvet Retreat)
2815 SW Harlow Ave
Portland, OR 97099
Call or Text: 1-555-714-3928
www.MarigoldNailsnSpa.example
Open 7 days a week.
After 7:00 PM is by appointment only.
Closed only on Thanksgiving & Christmas.

Target Market(s)

20%Man and 80%Woman 13-70

Industry/Entity Type

Business

Contact Information for Business Card

Elegant with Logo-Business name- address-phone-open days. closed day.

Font styles to use
Decorative
Script

Colors
000000

Requirements
Must have
• Logo and place for Technician Name
• Marigold Nails & Spa
• (The Velvet Retreat)
• 2815 SW Harlow Ave
• Portland, OR 97099
• Call or Text: 1-555-714-3928
• Open 7 days a week
• Closed only on Thanksgiving & Christmas.
• We accepted all major credit cards but prefer cash. Thank you
Nice to have
• Nail polish bottle with our Logo or letter M
Should not have
• too colorful

```html
<!DOCTYPE html>
<html lang="en">
<head>
<meta charset="utf-8">
<title>Marigold Nails &amp; Spa — Business Card</title>
<link rel="stylesheet" href="https://fonts.googleapis.com/css2?family=Montserrat:wght@400;500;600;700&display=swap">
<style>
  :root {
    --stage: #e9e9eb;
    --card-black: #050505;
    --salon-red: #e8222d;
    --accent-lime: #a3d02c;
    --text-white: #ffffff;
    --text-soft: #e6e6e6;
    --badge-light: #f2f2f2;
    --badge-mid: #d9d9d9;
    --polish-pink: #d99aa6;
    --polish-cap: #f7f3f3;
  }
  * { box-sizing: border-box; margin: 0; padding: 0; }
  html, body { width: 1200px; height: 900px; overflow: hidden; }
  body {
    background: var(--stage);
    font-family: "Montserrat", Arial, sans-serif;
    display: flex;
    flex-direction: column;
    align-items: center;
    justify-content: center;
    gap: 44px;
  }
  .card {
    position: relative;
    width: 660px;
    height: 378px;
    border-radius: 22px;
    background: var(--card-black);
    overflow: hidden;
    color: var(--text-white);
    box-shadow: 0 10px 24px rgba(0,0,0,0.18);
  }

  /* brand lockup */
  .brand { position: absolute; display: flex; flex-direction: column; align-items: flex-start; }
  .brand-row { display: flex; align-items: center; gap: 12px; }
  .brand-dot { width: 14px; height: 14px; border-radius: 50%; background: var(--text-white); }
  .brand-name { font-weight: 600; font-size: 34px; color: var(--text-white); letter-spacing: 0.5px; }
  .brand-tagline { margin-top: 6px; margin-left: 26px; font-size: 11px; font-weight: 500; letter-spacing: 3px; text-transform: uppercase; color: var(--text-soft); }

  /* front */
  .card-front .brand { left: 70px; top: 110px; }
  .payment-badges { position: absolute; right: 58px; top: 222px; display: flex; gap: 10px; }
  .payment-badge { width: 58px; height: 36px; border-radius: 4px; background: var(--badge-light); }
  .payment-badge:nth-child(even) { background: var(--badge-mid); }
  .payment-note {
    position: absolute; left: 0; right: 0; bottom: 44px;
    text-align: center; font-size: 16px; font-weight: 600; color: var(--accent-lime);
  }

  /* back */
  .red-band { position: absolute; inset: 0; width: 660px; height: 378px; }
  .hours { position: absolute; left: 150px; top: 34px; text-align: center; }
  .hours-open { color: var(--salon-red); font-size: 15px; font-weight: 600; }
  .hours-closed { color: var(--text-white); font-size: 15px; font-weight: 500; margin-top: 2px; }
  .card-back .brand { left: 160px; top: 102px; }
  .card-back .brand-name { font-size: 28px; }
  .polish-bottle {
    position: absolute; right: 40px; top: 26px; width: 70px; height: 140px;
    border-radius: 8px 8px 14px 14px;
    background: linear-gradient(180deg, var(--polish-cap) 0%, var(--polish-cap) 38%, var(--polish-pink) 42%, var(--polish-pink) 100%);
  }
  .technician { position: absolute; left: 56px; top: 236px; }
  .technician-name { font-size: 26px; font-weight: 700; }
  .technician-role { font-size: 14px; font-weight: 500; margin-bottom: 8px; }
  .contact-line { font-size: 15px; font-weight: 500; line-height: 1.35; }
  .contact-label { font-weight: 700; }
</style>
</head>
<body>

  <section class="card card-front">
    <div class="brand">
      <div class="brand-row">
        <span class="brand-dot"></span>
        <span class="brand-name">Marigold Nails &amp; Spa</span>
      </div>
      <span class="brand-tagline">The Velvet Retreat</span>
    </div>
    <div class="payment-badges">
      <span class="payment-badge"></span>
      <span class="payment-badge"></span>
      <span class="payment-badge"></span>
      <span class="payment-badge"></span>
    </div>
    <p class="payment-note">We accepted all major credit cards but prefer cash. Thank you</p>
  </section>

  <section class="card card-back">
    <svg class="red-band" viewBox="0 0 660 378" aria-hidden="true">
      <path d="M0 236 H470 C545 236 555 160 620 160 H660 V378 H0 Z" fill="var(--salon-red)"/>
    </svg>
    <div class="hours">
      <p class="hours-open">Open 7 days a week</p>
      <p class="hours-closed">Closed only on Thanksgiving &amp; Christmas</p>
    </div>
    <div class="brand">
      <div class="brand-row">
        <span class="brand-dot"></span>
        <span class="brand-name">Marigold Nails &amp; Spa</span>
      </div>
      <span class="brand-tagline">The Velvet Retreat</span>
    </div>
    <div class="polish-bottle" role="img" aria-label="Nail polish bottle illustration with the letter M on its label"></div>
    <div class="technician">
      <p class="technician-name">Dana Whitfield</p>
      <p class="technician-role">Director</p>
      <p class="contact-line">2815 SW Harlow Ave</p>
      <p class="contact-line">Portland, OR 97099</p>
      <p class="contact-line"><span class="contact-label">P:</span> 1-555-714-3928</p>
    </div>
  </section>

</body>
</html>
```